Redesign business cards

We have a new logo and I am not that happy with the layout of our existing card and looking for a change. Font is a bit small and the green can be hard to read. Logo may need a tidy up as the copy I have is not that hi-res too so require you to produce a hi-res version of the logo for us too. There will be three individual business cards to produce with just the names and phone numbers being different. Address will change too, but use what you see on the card for now.

Industry/Entity Type

Business

Requirements
Nice to have
• You could consider a redesign to the new logo, just not too radical. We like the blue and green hexagons as we feel that they are representative of oil industry that we are in.

```html
<!DOCTYPE html>
<html lang="en">
<head>
<meta charset="utf-8">
<title>NovaLube Oil Services – Business Card</title>
<link rel="stylesheet" href="https://fonts.googleapis.com/css2?family=Cabin:wght@400;600;700&family=Marcellus&display=swap">
<style>
  :root {
    --card-white: #ffffff;
    --brand-green: #9dcb07;
    --brand-blue: #0cb1e3;
    --name-cyan: #22b7e6;
    --title-teal: #0f3b3b;
    --ink: #1b1b1b;
    --divider: #9a9a9a;
    --address-white: #ffffff;
  }
  html, body {
    margin: 0;
    padding: 0;
    width: 1200px;
    height: 777px;
    overflow: hidden;
    background: var(--card-white);
  }
  .business-card {
    position: relative;
    width: 1200px;
    height: 777px;
    background: var(--card-white);
    overflow: hidden;
    font-family: "Cabin", sans-serif;
  }
  .card-wave {
    position: absolute;
    inset: 0;
    width: 1200px;
    height: 777px;
  }
  .brand {
    position: absolute;
    left: 56px;
    top: 160px;
    display: flex;
    align-items: center;
    gap: 22px;
  }
  .brand-mark {
    width: 38px;
    height: 38px;
    background: var(--brand-blue);
  }
  .brand-name {
    font-family: "Cabin", sans-serif;
    font-weight: 700;
    font-size: 100px;
    line-height: 1;
    color: var(--brand-green);
    letter-spacing: -1px;
  }
  .person {
    position: absolute;
    left: 56px;
    top: 340px;
  }
  .person-name {
    margin: 0;
    font-weight: 400;
    font-size: 37px;
    line-height: 1.2;
    color: var(--name-cyan);
    white-space: nowrap;
  }
  .person-title {
    margin: 10px 0 0;
    font-weight: 400;
    font-size: 37px;
    line-height: 1.2;
    color: var(--title-teal);
  }
  .divider {
    position: absolute;
    left: 680px;
    top: 155px;
    width: 2px;
    height: 388px;
    background: var(--divider);
  }
  .contact-list {
    position: absolute;
    left: 718px;
    top: 252px;
    margin: 0;
    padding: 0;
    list-style: none;
    font-family: "Marcellus", serif;
    font-size: 35px;
    color: var(--ink);
    white-space: nowrap;
  }
  .contact-list li {
    height: 68px;
    line-height: 68px;
  }
  .address {
    position: absolute;
    left: 472px;
    top: 670px;
    margin: 0;
    font-weight: 600;
    font-size: 24px;
    line-height: 34px;
    color: var(--address-white);
    font-style: normal;
    white-space: nowrap;
  }
</style>
</head>
<body>
  <main class="business-card">
    <svg class="card-wave" viewBox="0 0 1200 777" aria-hidden="true">
      <path fill="var(--brand-blue)" d="M0 690 C 320 650, 760 545, 1200 512 L1200 530 C 760 568, 320 700, 0 740 Z"/>
      <path fill="var(--brand-green)" d="M0 728 C 320 690, 760 570, 1200 528 L1200 777 L0 777 Z"/>
    </svg>

    <div class="brand">
      <span class="brand-name">NovaLube</span>
      <span class="brand-mark" aria-hidden="true"></span>
    </div>

    <div class="person">
      <h1 class="person-name">Daniel Whitford NZCE (Mech) P&amp;P</h1>
      <p class="person-title">Director</p>
    </div>

    <div class="divider" aria-hidden="true"></div>

    <ul class="contact-list">
      <li>P : +614 555 01937</li>
      <li>E : daniel@verdaclean.co.nz</li>
      <li>W : www.novalube.com.au</li>
    </ul>

    <address class="address">
      NovaLube Oil Services 418 Harbour Road|PO Box 5107|<br>
      Kelvin Grove Queensland 4059
    </address>
  </main>
</body>
</html>
```